online jewellery store business card

all black business card, glossy, with gold writing, gold logo and name (provided). simple design.

Target Market(s)

This business card is to put with purchases, so it just needs the logo and name Velmora Jewellery which I have uploaded pictures for you to use. Then it needs the web address, bidlorn address, email address and then the like us on KL for 10% off. All words to be used have been provided. Thanks

Industry/Entity Type

Store

Contact Information for Business Card

www.velmorajewellery.com
stores.bidlorn.com.au/Velmora-Jewellery
info@velmorajewellery.com

Like us on kinloop for 10% off your next purchase!

Requirements
Must have
• black background
gold writing
glossy look
Should not have
• yellow writing

```html
<!DOCTYPE html>
<html lang="en">
<head>
<meta charset="utf-8">
<title>Velmora Jewellery – Business Card</title>
<link href="https://fonts.googleapis.com/css2?family=Lato:wght@300;400&display=swap" rel="stylesheet">
<style>
  :root {
    --stage: #2a2622;
    --card-black: #060606;
    --panel-top: #1a1a1a;
    --panel-mid: #4a4a4a;
    --gold: #d4a85c;
    --gold-soft: #c9a063;
    --rule: #000000;
  }
  * { margin: 0; padding: 0; box-sizing: border-box; }
  html, body {
    width: 1200px; height: 900px; overflow: hidden;
    background: var(--stage);
    font-family: "Lato", Arial, sans-serif;
  }
  .stage {
    width: 1200px; height: 900px;
    display: flex; justify-content: center; align-items: center; gap: 60px;
  }
  .card {
    position: relative;
    width: 380px; height: 640px;
    border-radius: 18px;
    background: var(--card-black);
    overflow: hidden;
    box-shadow: 0 12px 30px rgba(0,0,0,0.45);
  }
  /* back of card */
  .card-back .brand-mark {
    position: absolute; left: 50%; top: 50%;
    transform: translate(-50%, -50%);
    display: flex; flex-direction: column; align-items: center; gap: 22px;
  }
  .mark-circle {
    width: 150px; height: 150px; border-radius: 50%;
    border: 2px solid var(--gold);
  }
  .mark-name {
    color: var(--gold); font-weight: 300;
    font-size: 24px; letter-spacing: 4px; text-transform: uppercase;
    text-align: center; line-height: 1.4;
  }
  /* front of card */
  .card-front .brand-head {
    position: absolute; left: 0; right: 0; top: 58px;
    display: flex; flex-direction: column; align-items: center;
  }
  .head-circle {
    width: 92px; height: 92px; border-radius: 50%;
    border: 1.5px solid var(--gold);
    margin-bottom: 18px;
  }
  .brand-name {
    color: var(--gold); font-weight: 300;
    font-size: 28px; letter-spacing: 5px; text-transform: uppercase;
    text-align: center; line-height: 1.3;
  }
  .info-panel {
    position: absolute; left: 0; top: 0; width: 380px; height: 640px;
  }
  .contact-list {
    position: absolute; left: 0; right: 0; top: 395px;
    list-style: none; text-align: center;
  }
  .contact-list li {
    color: var(--gold); font-size: 19px; font-weight: 400;
    margin-bottom: 34px;
  }
  .offer {
    position: absolute; left: 0; right: 0; bottom: 22px;
    text-align: center; color: var(--gold-soft);
    font-size: 14px; font-weight: 400;
  }
</style>
</head>
<body>
<main class="stage">
  <section class="card card-back" aria-label="Card back">
    <div class="brand-mark">
      <div class="mark-circle"></div>
      <div class="mark-name">Velmora<br>Jewellery</div>
    </div>
  </section>

  <section class="card card-front" aria-label="Card front">
    <svg class="info-panel" viewBox="0 0 380 640" aria-hidden="true">
      <defs>
        <radialGradient id="panelSheen" cx="0.45" cy="0.6" r="0.7">
          <stop offset="0" stop-color="#5a5a5a"/>
          <stop offset="0.6" stop-color="#2c2c2c"/>
          <stop offset="1" stop-color="#111111"/>
        </radialGradient>
      </defs>
      <path d="M0 330 C 90 300, 230 300, 380 318 L380 640 L0 640 Z" fill="url(#panelSheen)"/>
      <path d="M0 344 C 90 314, 230 314, 380 332" fill="none" stroke="#000" stroke-width="2"/>
      <path d="M0 358 C 90 328, 230 328, 380 346" fill="none" stroke="#000" stroke-width="1.5"/>
    </svg>
    <header class="brand-head">
      <div class="head-circle"></div>
      <h1 class="brand-name">Velmora<br>Jewellery</h1>
    </header>
    <ul class="contact-list">
      <li>www.velmorajewellery.com</li>
      <li>bidlorn.com.au/Velmora-Jewellery</li>
      <li>info@velmorajewellery.com</li>
    </ul>
    <p class="offer">Like us on kinloop for 10% off your next purchase!</p>
  </section>
</main>
</body>
</html>
```